"The Quiet Mirror" Musical Theatre Poster Design

Hi there! I need a poster design for a new youth musical I'm writing called "The Quiet Mirror".

The story is about a girl called Terri who is the most popular girl in the school. However, after a horrible accident, Terri is confined to a wheelchair. Not only does she have to deal with coming to terms with her life in a wheelchair, but she also has to make new friends after her old group of friends decide that she no longer fits their idea of 'perfect'. It's a powerful, modern story that uses contemporary music, technology but also hits at the heart of the teenage social experience.

Musically, the styles include pop, RnB, and pop/rock.

As for what I need in the poster - I'm not really sure! I'm looking for something that:
- uses the title "The Quiet Mirror" in a unique way
- doesn't necessarily use a wheelchair as an image
- would appeal to a 10-15 year old audience (so not too childish, more teen or tween), yet has a sense of seriousness to it. The musical is dramatic and deals with some confronting issues.
- includes "A New Musical by Maya Fitch"

As for colours, etc. surprise me! Sorry I can't be more specific but I haven't even really got a visual on it at all.

If you would like some demo recordings of the music, just let me know!

I've also attached some poster that I really like - more of a reference point of how a musical theatre poster should look.

Target Market(s)

Teens and adults

Font styles to use
Serif
Sans Serif

Colors

Designer to choose colors to be used in the design.

Requirements
Nice to have
• * perhaps use the concept of "different" and "normal" as two opposite yet somehow similar words.
• * maybe use of circles to symbolise a wheelchair but also having to start again, circular nature of life, rebirth, renewal?
Should not have
• - not any instruments in the design. The poster is for a theatrical musical, not a pop group, or singular song.

```html
<!DOCTYPE html>
<html lang="en">
<head>
<meta charset="utf-8">
<title>The Quiet Mirror – Poster</title>
<link rel="stylesheet" href="https://fonts.googleapis.com/css2?family=Bowlby+One+SC&family=Federo&display=swap">
<style>
  :root {
    --red-bright: #e8130f;
    --red-mid: #b40a08;
    --red-deep: #6e0604;
    --red-shadow: #3a0201;
    --band: #2a0101;
    --title-yellow: #e9e12a;
    --title-ochre: #c9b51c;
  }
  html, body {
    margin: 0;
    padding: 0;
    width: 924px;
    height: 1200px;
    overflow: hidden;
    background: #ffffff;
  }
  .poster {
    position: relative;
    width: 924px;
    height: 1200px;
    overflow: hidden;
    background: var(--red-deep);
  }
  .poster__art {
    position: absolute;
    inset: 0;
    background:
      radial-gradient(ellipse 46% 58% at 60% 42%, var(--red-bright) 0%, var(--red-mid) 55%, transparent 80%),
      radial-gradient(ellipse 40% 30% at 35% 78%, var(--red-mid) 0%, transparent 75%),
      linear-gradient(160deg, var(--red-deep) 0%, var(--red-mid) 45%, var(--red-shadow) 100%);
  }
  .poster__shards {
    position: absolute;
    inset: 0;
    width: 924px;
    height: 1200px;
  }
  .poster__title {
    position: absolute;
    left: 0;
    top: 0;
    width: 924px;
    margin: 0;
    color: var(--title-yellow);
    text-shadow: 0 0 1px var(--title-ochre);
    font-weight: 400;
  }
  .title__small,
  .title__large,
  .title__wide {
    position: absolute;
    display: block;
    line-height: 1;
    white-space: nowrap;
  }
  .title__small {
    top: 168px;
    left: 360px;
    font-family: "Federo", sans-serif;
    font-size: 88px;
    transform: scaleY(1.45);
    transform-origin: top left;
    letter-spacing: 2px;
  }
  .title__wide {
    top: 316px;
    left: 150px;
    width: 640px;
    text-align: center;
    font-family: "Bowlby One SC", sans-serif;
    font-size: 118px;
    letter-spacing: 6px;
  }
  .title__large {
    top: 452px;
    left: 222px;
    font-family: "Federo", sans-serif;
    font-size: 108px;
    transform: scaleY(1.22);
    transform-origin: top left;
    letter-spacing: 1px;
  }
  .poster__band {
    position: absolute;
    left: 0;
    bottom: 0;
    width: 924px;
    height: 162px;
    background: linear-gradient(180deg, rgba(58,2,1,0.85), var(--band));
  }
  .poster__credit {
    position: absolute;
    left: 0;
    bottom: 52px;
    width: 924px;
    margin: 0;
    text-align: center;
    font-family: "Federo", sans-serif;
    font-size: 44px;
    line-height: 1;
    letter-spacing: 3px;
    color: var(--title-yellow);
    transform: scaleY(1.2);
    transform-origin: bottom center;
  }
</style>
</head>
<body>
  <main class="poster">
    <div class="poster__art" role="img" aria-label="Red-toned close-up photograph of a girl's face with closed eyes, overlaid with a large eye, in a shattered-glass texture"></div>

    <svg class="poster__shards" viewBox="0 0 924 1200" aria-hidden="true">
      <polygon points="0,0 260,0 0,420" fill="#2a0201" opacity="0.45"/>
      <polygon points="0,560 500,230 924,0 924,160 0,760" fill="#3a0201" opacity="0.25"/>
      <polygon points="924,0 924,520 640,0" fill="#1e0100" opacity="0.35"/>
      <polygon points="0,820 420,1040 0,1040" fill="#2a0201" opacity="0.35"/>
      <polygon points="924,700 924,1040 560,1040" fill="#2a0201" opacity="0.4"/>
      <line x1="0" y1="120" x2="924" y2="980" stroke="#1e0100" stroke-width="2" opacity="0.35"/>
      <line x1="924" y1="220" x2="80" y2="1040" stroke="#1e0100" stroke-width="2" opacity="0.3"/>
      <line x1="300" y1="0" x2="780" y2="1040" stroke="#1e0100" stroke-width="1.5" opacity="0.3"/>
    </svg>

    <h1 class="poster__title">
      <span class="title__small">THE</span>
      <span class="title__wide">QUIET</span>
      <span class="title__large">MIRROR</span>
    </h1>

    <div class="poster__band"></div>
    <p class="poster__credit">A NEW MUSICAL BY MAYA FITCH</p>
  </main>
</body>
</html>
```